**** Web design project for VornaSoft ****

For my ICT company VornaSoft I need a website.

We design, build and host web-applications and we have our own CMS product. In the references part we want to show sample websites (thumbnails) + links.

It should look modern (WEB 2.0), rounded corners.

I want the following menu' s:
- Home
- Services
- References
- News
- About VornaSoft
- Contact

Sample websites:
See attachments
http://www.plumvest.com
http://www.gadomirbureauwerk.nl

Reason: Want to take some time for feedback and improvements.

Reason: I'm waiting for a black background, with shadow and ambient light. You'll make a good chance!

Industry/Entity Type

It Company

Requirements
Must have
• - Fixed width (1024px), should fit on an IPad2
- Language selection English/Dutch
- Twitter/Facebook/LinkedIn/RSS icons
- Footer for Terms of use and Copyrights
- Search box
- 3 (or more) boxes for information i.e. news, blog or advertisements
Nice to have
• - Footer Site Map
- Contrasting background outside borders
- wide image (rotator) (with transperant sentence block)
- Shadow

```html
<!DOCTYPE html>
<html lang="en">
<head>
<meta charset="utf-8">
<title>VornaSoft</title>
<link href="https://fonts.googleapis.com/css2?family=Gelasio:wght@400;700&family=Fira+Sans:wght@500;700&display=swap" rel="stylesheet">
<style>
:root{
  --page:#3b2b3e;
  --header:#262029;
  --gold:#f2b705;
  --gold-light:#f6c844;
  --ink:#2a2430;
  --card:#e5d7b4;
  --card-edge:#cbbb92;
  --news:#0e1920;
  --cream:#f7e6a8;
  --white:#ffffff;
  --muted:#4a4050;
}
*{box-sizing:border-box;margin:0;padding:0}
html,body{width:1135px;height:1200px;overflow:hidden}
body{background:var(--page);font-family:"Gelasio",Georgia,serif;position:relative}
.site{position:absolute;left:113px;top:0;width:911px;height:1200px}

.topbar{position:absolute;left:0;top:0;width:911px;height:31px;background:var(--gold);border-radius:0 0 6px 6px}
.utility{position:absolute;right:0;top:16px;width:190px;height:30px;background:var(--gold);border-radius:0 0 6px 6px;
  display:flex;gap:8px;justify-content:center;align-items:center;font:700 12px "Fira Sans",sans-serif;color:var(--ink)}
.header{position:absolute;left:0;top:31px;width:911px;height:112px;background:linear-gradient(#2f2734,var(--header));z-index:-1}
.brand{position:absolute;left:8px;top:56px;display:flex;align-items:center;gap:12px}
.brand-mark{width:40px;height:40px;border-radius:50%;background:#2c9ed8}
.brand-name{font-family:"Fira Sans",sans-serif;font-weight:500;font-size:28px;color:#9fb3c4}
.search{position:absolute;left:692px;top:85px;width:190px;height:31px;border:3px solid #5b5560;border-radius:6px;background:var(--gold);display:flex;overflow:hidden}
.search-field{flex:0 0 120px;display:flex;align-items:center;justify-content:space-between;padding:0 10px;font:500 14px "Fira Sans",sans-serif;color:var(--ink)}
.search-go{flex:1;background:#2a2430;color:var(--gold);display:flex;align-items:center;justify-content:center;font:700 15px "Fira Sans",sans-serif;border-left:2px solid #1a161c}

.nav{position:absolute;left:0;top:143px;width:911px;height:46px}
.nav a{position:absolute;top:0;height:46px;background:var(--gold);border-radius:5px 5px 0 0;text-decoration:none;
  display:flex;align-items:center;justify-content:center;font:700 20px "Fira Sans",sans-serif;color:var(--ink)}
.nav a.current{background:var(--gold-light);color:#fbe9b2}

.hero{position:absolute;left:3px;top:189px;width:907px;height:382px;background:linear-gradient(120deg,#d8cdb6,#b9a98c 55%,#7e6f5c);overflow:hidden}
.hero-caption{position:absolute;left:0;bottom:0;width:100%;height:80px;background:rgba(230,222,205,.55);padding:16px 85px 0 0;
  font:700 16px/20px "Gelasio",serif;color:#1c1820}
.hero-dots{position:absolute;right:47px;bottom:15px;display:flex;gap:8px}
.hero-dots span{width:17px;height:17px;border-radius:50%;background:#c9c2b6}
.hero-dots span.active{background:var(--gold)}

.service{position:absolute;top:573px;height:179px;background:var(--card);border:1px solid var(--card-edge);border-radius:5px;box-shadow:3px 4px 6px rgba(0,0,0,.4)}
.service h2{position:absolute;left:44px;top:18px;font:700 20px "Gelasio",serif;color:var(--muted)}
.service p{position:absolute;left:34px;top:52px;width:160px;font:400 11px/15px "Gelasio",serif;letter-spacing:.2px;color:#3a2f25}
.service svg{position:absolute;right:14px;top:4px}
.btn{position:absolute;width:74px;height:32px;background:var(--gold);border-radius:4px;color:var(--cream);
  font:700 16px "Fira Sans",sans-serif;display:flex;align-items:center;justify-content:center;text-decoration:none}
.service .btn{left:178px;top:124px}

.welcome{position:absolute;left:44px;top:772px;width:452px}
.welcome h1{font:700 20px "Gelasio",serif;color:var(--cream)}
.welcome p{margin-top:18px;font:700 16px/19px "Gelasio",serif;color:var(--cream)}
.welcome .btn{left:155px;top:290px}

.news{position:absolute;left:663px;top:756px;width:248px;height:332px;background:var(--news);border-radius:0 0 5px 5px;box-shadow:3px 4px 6px rgba(0,0,0,.4)}
.news-head{position:absolute;left:22px;top:18px;display:flex;align-items:center;gap:16px}
.news h2{font:700 20px "Gelasio",serif;color:var(--cream)}
.news p{position:absolute;left:9px;top:68px;width:232px;font:400 11px/15px "Gelasio",serif;letter-spacing:.3px;color:#f8ec9a}
.news .btn{left:133px;top:266px}

.footer{position:absolute;left:0;top:1134px;width:911px;height:53px;background:var(--gold);border-radius:5px;display:flex;align-items:center;
  padding-left:26px;font:500 14px "Fira Sans",sans-serif;color:var(--ink)}
.footer .copy{margin-left:24px}
.social{position:absolute;left:666px;top:6px;display:flex;gap:4px}
.social span{width:40px;height:40px;border-radius:7px;border:2px solid #fff}
.social .rss{background:#f07d1a}.social .in{background:#1b7bb0}.social .fb{background:#3b5b98}.social .tw{background:#4cb8e6}
</style>
</head>
<body>
<div class="site">
  <div class="topbar"></div>
  <div class="header"></div>
  <div class="utility"><span>Dutch</span><span>English</span><span>Login</span></div>
  <div class="brand"><span class="brand-mark"></span><span class="brand-name">VornaSoft</span></div>
  <div class="search">
    <div class="search-field">search
      <svg width="22" height="18" viewBox="0 0 22 18"><circle cx="8" cy="7" r="5.5" fill="none" stroke="#2a2430" stroke-width="2.5"/><line x1="12" y1="11" x2="19" y2="16" stroke="#2a2430" stroke-width="3"/></svg>
    </div>
    <div class="search-go">go</div>
  </div>

  <nav class="nav">
    <a class="current" href="#" style="left:0;width:138px">Home</a>
    <a href="#" style="left:156px;width:135px">Services</a>
    <a href="#" style="left:307px;width:136px">References</a>
    <a href="#" style="left:462px;width:136px">News</a>
    <a href="#" style="left:622px;width:136px">About</a>
    <a href="#" style="left:774px;width:137px">Contact</a>
  </nav>

  <section class="hero" role="img" aria-label="Rotating banner photo of a business team in front of sketched diagrams">
    <div class="hero-caption">Lorem Ipsum is simply dummy text of the printing and typesetting industry. Lorem Ipsum has been the industry's standard dummy text</div>
    <div class="hero-dots"><span class="active"></span><span></span><span></span></div>
  </section>

  <article class="service" style="left:2px;width:296px">
    <h2>Service 1</h2>
    <svg width="60" height="60" viewBox="0 0 60 60" aria-hidden="true"><circle cx="30" cy="30" r="27" fill="#3aa0e0"/><ellipse cx="30" cy="30" rx="12" ry="27" fill="none" stroke="#8ccf4a" stroke-width="4"/><line x1="3" y1="30" x2="57" y2="30" stroke="#8ccf4a" stroke-width="4"/></svg>
    <p>Lorem Ipsum is simply dummy text of the printing and typesetting industry. Lorem Ipsum has been the industry's standard dummy text</p>
    <a class="btn" href="#">more</a>
  </article>
  <article class="service" style="left:308px;width:295px">
    <h2>Service 2</h2>
    <svg width="66" height="60" viewBox="0 0 66 60" aria-hidden="true"><circle cx="32" cy="30" r="27" fill="#e9ecef"/><path d="M36 28 L63 24 A27 27 0 0 1 60 42 Z" fill="#bde04a"/><path d="M36 28 L60 42 A27 27 0 0 1 52 50 Z" fill="#4ab0e8"/></svg>
    <p>Lorem Ipsum is simply dummy text of the printing and typesetting industry. Lorem Ipsum has been the industry's standard dummy text</p>
    <a class="btn" href="#">more</a>
  </article>
  <article class="service" style="left:616px;width:295px">
    <h2>Service 3</h2>
    <svg width="70" height="56" viewBox="0 0 70 56" aria-hidden="true"><path d="M2 16 L20 2 V10 H40 V22 H20 V30 Z" fill="#8ccf3a"/><path d="M68 38 L48 22 V30 H26 V46 H48 V54 Z" fill="#3a9fe6"/></svg>
    <p>Lorem Ipsum is simply dummy text of the printing and typesetting industry. Lorem Ipsum has been the industry's standard dummy text</p>
    <a class="btn" href="#">more</a>
  </article>

  <section class="welcome">
    <h1>Welcome to VornaSoft</h1>
    <p>Lorem Ipsum is simply dummy text of the printing and typesetting industry. Lorem Ipsum has been the industry's standard dummy text ever since the 1500s, when an unknown printer took a galley of type and scrambled it to make a type specimen book. It has survived not only five centuries, but also the leap into electronic typesetting, remaining essentially unchanged. It was popularised in the 1960s with the release of Tavelmark sheets containing Lorem Ipsum passages, and more recently with desktop publishing software like Quorrin LayoutDesk including versions of Lorem Ipsum.</p>
    <a class="btn" href="#">more</a>
  </section>

  <aside class="news">
    <div class="news-head">
      <svg width="36" height="36" viewBox="0 0 36 36" aria-hidden="true"><path d="M4 13 H12 L28 4 V32 L12 23 H4 Z" fill="#dfe6ee"/><rect x="8" y="23" width="6" height="10" fill="#3a8fd0"/></svg>
      <h2>Latest News</h2>
    </div>
    <p>Lorem ipsum dolor sit amet, consectetur adipisicing elit, sed do eiusmod tempor incididunt ut labore et dolore magna aliqua. Ut enim ad minim veniam, quis nostrud exercitation ullamco laboris nisi ut aliquip ex ea commodo consequat. Duis aute irure dolor in reprehenderit in voluptate velit esse cillum dolore eu fugiat nulla pariatur. Excepteur sint occaecat cupidatat non proident, sunt in culpa qui officia deserunt mollit anim id est laborum.</p>
    <a class="btn" href="#">more</a>
  </aside>

  <footer class="footer">
    <span>Terms of Use</span>
    <span class="copy">©copyrightvornasoft2012</span>
    <div class="social">
      <span class="rss" role="img" aria-label="RSS feed"></span>
      <span class="in" role="img" aria-label="Professional network"></span>
      <span class="fb" role="img" aria-label="Social network"></span>
      <span class="tw" role="img" aria-label="Microblog"></span>
    </div>
  </footer>
</div>
</body>
</html>
```